Professional Personal Website with Blog and four sections

I am seeking a website design for myself. I would like the site to contain a blog, related to Information Security and several sections.

I am an established Information Security Consultant (one aspect of the site).
I am an author of a children's spiritual book that is "new thought" (another aspect of the site)
I am a co-founder of a secure social platform for kids and families (www.tovarelo.net)
I may want a section on finance as well, not sure at this moment

I want this site to be a personal website, not a subscription service or professional services sales site, I want the site to look very professional, so that I can share it with all types of people without concern - business, spiritual, other.

I have provided a photo of myself for the site, smart casual on a beach. The site will be hosted on brennmorlock.net

You can see samples of what I am referring to by searching "personal website" on images.zumvaro.net

I would like the page layout, and the images chopped up as individual jpgs, including hover images for buttons. I can do the coding

I would like the following buttons
Home, About, Information Security Blog, Passion Projects, Contact

I would like the top portion of the page to say "Dorian Pell"
I would like the subtext to say:
Executive Information Security Architect, Author, and Idea Man

I envision the following

Target Market(s)

Executive / Technical / Creative types / Spritual types

Number of Pages Required

4 page

Requirements
Must have
• Blog section
Should not have
• No Matrix themes or No Cop themes, No Fingerprints or Eyeball scans

```html
<!DOCTYPE html>
<html lang="en">
<head>
<meta charset="utf-8">
<title>Dorian Pell</title>
<link rel="stylesheet" href="https://fonts.googleapis.com/css2?family=Open+Sans:wght@400;600;700&display=swap">
<style>
:root{
  --yellow:#f5b800;
  --dark:#1e1e1e;
  --darker:#161616;
  --grey-text:#777;
  --title:#444;
  --white:#fff;
}
*{box-sizing:border-box;margin:0;padding:0}
html,body{width:667px;height:1200px;overflow:hidden}
body{font-family:"Open Sans",Arial,sans-serif;background:var(--white);color:var(--title)}
.page{width:667px;height:1200px;position:relative}

.site-header{height:56px;background:var(--dark);display:flex;align-items:center;justify-content:space-between;padding:0 22px 0 18px}
.brand{font-size:21px;color:var(--white);letter-spacing:1px;text-transform:uppercase;font-weight:400}
.main-nav{display:flex;gap:4px}
.main-nav a{color:var(--white);font-size:9px;text-decoration:none;padding:5px 9px}
.main-nav a.active{background:var(--white);color:var(--dark)}

.hero{height:289px;position:relative}
.hero-photo{position:absolute;inset:0;background:linear-gradient(180deg,#8fb3d4 0%,#b9cfe0 45%,#6f8ea8 62%,#8a8377 80%,#5c5a55 100%)}
.hero-tagline{position:absolute;left:44px;top:190px;font-size:18px;line-height:26px;color:var(--white);font-weight:400}
.hero-tagline em{font-style:normal;color:var(--yellow)}

.section-title{text-align:center;font-size:24px;font-weight:400;color:var(--title)}
.section-title span{color:var(--yellow)}

.about{height:155px;padding-top:18px}
.about p{width:590px;margin:14px auto 0;font-size:8.5px;line-height:14px;color:var(--grey-text);text-align:center}

.blog{height:222px;position:relative;padding-top:22px}
.blog-bg{position:absolute;inset:0;background:linear-gradient(180deg,#3a3a38,#242422)}
.blog .section-title{position:relative;color:var(--white)}
.blog-cards{position:relative;display:flex;justify-content:space-between;padding:0 45px;margin-top:16px}
.blog-card{width:167px}
.blog-thumb{height:82px;position:relative}
.thumb-1{background:linear-gradient(135deg,#2f6fb3,#79b0e0)}
.thumb-2{background:linear-gradient(135deg,#7a3b16,#c98a4a)}
.thumb-3{background:linear-gradient(135deg,#cfd3d6,#8a9198)}
.date-badge{position:absolute;left:6px;top:0;width:26px;height:30px;background:var(--yellow);color:var(--white);text-align:center;font-size:11px;font-weight:700;line-height:14px;padding-top:2px}
.date-badge small{display:block;font-size:6px;font-weight:600}
.blog-card h3{font-size:7px;color:var(--white);font-weight:700;margin-top:10px}
.blog-card p{font-size:6.5px;line-height:10px;color:#bbb;margin-top:4px}

.projects{height:255px;padding-top:44px}
.project-list{display:flex;justify-content:space-between;padding:0 44px;margin-top:22px}
.project{width:174px;height:93px;position:relative}
.proj-1{background:linear-gradient(135deg,#d9d9d9,#8e8e8e)}
.proj-2{background:linear-gradient(135deg,#c58a4e,#6e4120)}
.proj-3{background:linear-gradient(135deg,#9fc9e6,#4d86b8)}
.project-label{position:absolute;left:50%;bottom:0;transform:translateX(-50%);background:var(--yellow);color:var(--dark);font-size:7.5px;font-weight:600;padding:4px 10px;white-space:nowrap}

.contact{height:200px;position:relative;padding:14px 44px 0}
.contact-bg{position:absolute;inset:0;background:linear-gradient(135deg,#2c2c2c,#141414)}
.contact-inner{position:relative;display:flex;justify-content:space-between}
.contact-info{width:240px;color:var(--white)}
.contact-info h2{font-size:16px;font-weight:600}
.contact-info .intro{font-size:6.5px;line-height:10px;color:#ccc;margin-top:8px}
.contact-item{display:flex;align-items:center;gap:10px;margin-top:12px;font-size:7px;color:#ddd}
.contact-item svg{flex:none}
.contact-form{width:282px;display:flex;flex-direction:column;gap:6px;padding-top:2px}
.field{background:var(--white);height:14px;font-size:6.5px;color:#999;padding:3px 5px}
.field.message{height:60px}
.submit{align-self:center;background:var(--yellow);color:var(--dark);font-size:7px;font-weight:600;padding:4px 16px;margin-top:4px}

.site-footer{height:23px;background:var(--yellow);display:flex;align-items:center;padding:0 44px;font-size:7px;color:var(--dark)}
</style>
</head>
<body>
<div class="page">
  <header class="site-header">
    <div class="brand">Dorian Pell</div>
    <nav class="main-nav">
      <a class="active" href="#">Home</a>
      <a href="#">About</a>
      <a href="#">Information Security Blog</a>
      <a href="#">Passion Projects</a>
      <a href="#">Contact</a>
    </nav>
  </header>

  <section class="hero">
    <div class="hero-photo" role="img" aria-label="Portrait of Dorian Pell in a white shirt standing on a beach with the sea behind"></div>
    <h1 class="hero-tagline">Executive <em>Information Security</em><br><em>Architect</em> , <em>Author</em> &amp; <em>Idea Man</em></h1>
  </section>

  <section class="about">
    <h2 class="section-title">About <span>Me</span></h2>
    <p>Dorian Pell advises leadership teams on security architecture, risk and resilient design. Alongside that work he writes books for children about kindness, courage and wonder, and co-founded a safe social space where families can share and learn together. This site gathers his writing, his projects and the ideas that connect them, for anyone curious about building a calmer, safer digital world.</p>
  </section>

  <section class="blog">
    <div class="blog-bg" role="img" aria-label="Dark desk workspace background"></div>
    <h2 class="section-title">Latest <span>Blog</span></h2>
    <div class="blog-cards">
      <article class="blog-card">
        <div class="blog-thumb thumb-1" role="img" aria-label="Blue world map illustration"><div class="date-badge">21<small>JUN</small></div></div>
        <h3>DUIS AUTEM VEL EUM IRIURE DOLOR IN</h3>
        <p>Notes on threat modelling for small teams and why simple controls often matter most.</p>
      </article>
      <article class="blog-card">
        <div class="blog-thumb thumb-2" role="img" aria-label="Hand writing with a pen on paper"><div class="date-badge">14<small>JUN</small></div></div>
        <h3>DUIS AUTEM VEL EUM IRIURE DOLOR IN</h3>
        <p>What writing for children taught me about explaining complex security ideas clearly.</p>
      </article>
      <article class="blog-card">
        <div class="blog-thumb thumb-3" role="img" aria-label="Businessman in front of sketched ideas"><div class="date-badge">07<small>JUN</small></div></div>
        <h3>DUIS AUTEM VEL EUM IRIURE DOLOR IN</h3>
        <p>Ideas worth testing: building trust into products from the very first sketch.</p>
      </article>
    </div>
  </section>

  <section class="projects">
    <h2 class="section-title">Passion <span>Projects</span></h2>
    <div class="project-list">
      <div class="project proj-1" role="img" aria-label="Hands typing on a laptop keyboard"><span class="project-label">Information Security Blog</span></div>
      <div class="project proj-2" role="img" aria-label="Open notebook and pen on a wooden desk"><span class="project-label">Author</span></div>
      <div class="project proj-3" role="img" aria-label="Thinking man surrounded by drawn ideas"><span class="project-label">Idea Man</span></div>
    </div>
  </section>

  <section class="contact">
    <div class="contact-bg" role="img" aria-label="Dark laptop and desk background"></div>
    <div class="contact-inner">
      <div class="contact-info">
        <h2>Get in touch with us</h2>
        <p class="intro">Questions, speaking requests or project ideas are always welcome. Send a note below.</p>
        <div class="contact-item">
          <svg width="14" height="14" viewBox="0 0 14 14"><rect width="14" height="14" fill="#f5b800"/><path d="M7 3a2.5 2.5 0 0 0-2.5 2.5C4.5 8 7 11 7 11s2.5-3 2.5-5.5A2.5 2.5 0 0 0 7 3z" fill="#fff"/></svg>
          <span>240 Harbour Lane, Suite 12, Seaview</span>
        </div>
        <div class="contact-item">
          <svg width="14" height="14" viewBox="0 0 14 14"><rect width="14" height="14" fill="#f5b800"/><path d="M4.5 3.5l1.5 0 .8 2-1 .7a5 5 0 0 0 2.5 2.5l.7-1 2 .8v1.5c0 .4-.4.8-.8.8A6.5 6.5 0 0 1 3.7 4.3c0-.4.4-.8.8-.8z" fill="#fff"/></svg>
          <span>Tel: +1 555 014 2297</span>
        </div>
        <div class="contact-item">
          <svg width="14" height="14" viewBox="0 0 14 14"><rect width="14" height="14" fill="#f5b800"/><rect x="3" y="4.5" width="8" height="5.5" fill="none" stroke="#fff"/><path d="M3 4.5l4 3 4-3" fill="none" stroke="#fff"/></svg>
          <span>hello@brennmorlock.net</span>
        </div>
      </div>
      <div class="contact-form">
        <div class="field">Name</div>
        <div class="field">Email</div>
        <div class="field message">Message</div>
        <div class="submit">Submit</div>
      </div>
    </div>
  </section>

  <footer class="site-footer">Copyright 2015 Dorian Pell. All rights reserved.</footer>
</div>
</body>
</html>
```